Thabeni Academy one-page profile

I need to develop a professionally designed "one-pager" for a new independent school opening in the Mavuso Township in South Africa in 2015. Mavuso is one of the poorest communities in South Africa and our aim is to bring a university preparatory education to this community. The school will open with kindergarten students and will expand each year until we reach grade 12. I would like for the file to be in a format that I can easily edit in the event that the information that I provide in the attachment changes or should I choose to utilize the format for an additional flyer.

The document needs to be designed as an A4 paper sized document as opposed to the standard size used in the United States.

I like the format of the following document:
http://www.brelvonschools.org/pdfs/11.30.2012%20BNQS%20Tutoring%20One%20Pager.pdf
http://www.prindlework.com/images/150_Teacher_recruitment_flyer.jpg
http://slatehouse.org/2013/01/18/BRON%2520TQGS%2520Lottery%2520Information_English%2520Flyer%5B1%5D.jpg
Updates

I edited the attached Thabeni Academy one page profile by altering it slightly and cutting out some unnecessary wording.  Please view to make changes.

Target Market(s)

The target market for this piece are potential funders and partners.

Industry/Entity Type

University

Requirements
Must have
• The design must use the Thabeni Academy colors and fonts as outlined in the branding guide. The design must look professional and must give the impression of a stellar private school.
Should not have
• Clip art

```html
<!DOCTYPE html>
<html lang="en">
<head>
<meta charset="utf-8">
<title>Thabeni Academy – One-Page Profile</title>
<link href="https://fonts.googleapis.com/css2?family=Arimo:wght@400;700&display=swap" rel="stylesheet">
<style>
  :root {
    --blue-deep: #1b75bb;
    --blue-bright: #27a9e1;
    --ink: #231f20;
    --paper: #ffffff;
    --photo-dark: #4a4a4a;
    --photo-light: #9a9a9a;
  }
  * { margin: 0; padding: 0; box-sizing: border-box; }
  html, body { width: 1000px; height: 1200px; overflow: hidden; background: var(--paper); }
  body { position: relative; font-family: "Arimo", Arial, sans-serif; color: var(--ink); }

  .photo {
    position: absolute;
    background: linear-gradient(135deg, var(--photo-light), var(--photo-dark));
  }
  .photo--hero { left: 76px; top: 0; width: 849px; height: 408px;
    background: linear-gradient(120deg, #6f6f6f 0%, #bdbdbd 45%, #5c5c5c 100%); }
  .photo--reading { left: 76px; top: 418px; width: 442px; height: 250px;
    background: linear-gradient(160deg, #d9d9d9 0%, #8c8c8c 60%, #555 100%); }
  .photo--circle { left: 528px; top: 418px; width: 397px; height: 250px;
    background: linear-gradient(200deg, #bdbdbd 0%, #7a7a7a 55%, #3d3d3d 100%); }

  .accent-band { position: absolute; left: 76px; top: 600px; width: 849px; height: 124px; }

  .section { position: absolute; left: 102px; width: 796px; }
  .section__title {
    color: var(--blue-deep); font-weight: 700; font-size: 19px; letter-spacing: 0.1px;
  }
  .section__body { font-size: 12.6px; line-height: 21px; margin-top: 2px; }
  .section__body--justify { text-align: justify; }

  .core { top: 755px; }
  .leader { top: 957px; }

  .components { position: absolute; top: 843px; left: 100px; width: 800px; height: 80px; }
  .component {
    position: absolute; display: flex; align-items: center; gap: 10px;
    color: var(--blue-bright); font-weight: 700; font-size: 22px; white-space: nowrap;
  }
  .component__mark { width: 28px; height: 28px; flex: none; }
  .component--a { left: 0; top: 8px; }
  .component--b { left: 0; top: 43px; }
  .component--c { left: 518px; top: 10px; }
  .component--d { left: 518px; top: 45px; }

  .contact-bar {
    position: absolute; left: 76px; top: 1158px; width: 849px; height: 42px;
    background: var(--blue-bright); color: var(--paper);
    display: flex; align-items: center; gap: 10px; padding-left: 22px;
    font-weight: 700; font-size: 14px;
  }
  .contact-bar svg { width: 20px; height: 20px; }
</style>
</head>
<body>

  <div class="photo photo--hero" role="img" aria-label="Black and white photo of a mother reading a picture book with two young children in a library"></div>
  <div class="photo photo--reading" role="img" aria-label="Black and white photo of a small girl leafing through a book at a table"></div>
  <div class="photo photo--circle" role="img" aria-label="Black and white photo of a teacher reading to children seated on the library floor"></div>

  <svg class="accent-band" viewBox="0 0 849 124" preserveAspectRatio="none" aria-hidden="true">
    <polygon points="0,68 849,8 849,58 0,100" fill="var(--blue-bright)"/>
    <polygon points="0,60 849,60 849,120 300,88 0,92" fill="var(--blue-deep)"/>
    <polygon points="0,92 300,88 0,122" fill="var(--blue-bright)"/>
  </svg>

  <section class="section core">
    <h2 class="section__title">CORE COMPONENTS</h2>
    <p class="section__body">At Thabeni Academy, we have outlined four core components that will be prioritized; each area provides an avenue for achieving our mission of ensuring that all students are prepared with the academic and character skills that they need to be successful in university.</p>
  </section>

  <div class="components">
    <div class="component component--a">
      <svg class="component__mark" viewBox="0 0 28 28"><circle cx="14" cy="14" r="9" fill="var(--blue-deep)"/></svg>
      Social Justice Foundation
    </div>
    <div class="component component--b">
      <svg class="component__mark" viewBox="0 0 28 28"><circle cx="14" cy="14" r="9" fill="var(--blue-deep)"/></svg>
      Standards Based Unit and Lesson Planning
    </div>
    <div class="component component--c">
      <svg class="component__mark" viewBox="0 0 28 28"><circle cx="14" cy="14" r="9" fill="var(--blue-deep)"/></svg>
      Literacy Focus
    </div>
    <div class="component component--d">
      <svg class="component__mark" viewBox="0 0 28 28"><circle cx="14" cy="14" r="9" fill="var(--blue-deep)"/></svg>
      Date Driven Instrucion
    </div>
  </div>

  <section class="section leader">
    <h2 class="section__title">OUR SCHOOL LEADER</h2>
    <p class="section__body section__body--justify">Naledi Okafor-Dube is a passionate educator and advocate for social justice.&nbsp; She has served as a contributing writer for Learning Horizons Review and Classroom Voices and in 2012 Naledi gave a SparkTalks talk on the importance of an education steeped in social justice. Naledi is excited about the opportunity to learn and serve the Mavuso Township and is one of the organizers for SparkTalksMavuso.&nbsp; In 2013, Naledi completed the highly selective Brightpath Global Fellowship Programme, a specialized programme that prepares fellows to found and lead high performing schools in underserved communities. Prior to establishing Thabeni Academy, Naledi taught middle school humanities for seven years and worked as an education programme coordinator. Naledi holds an MS Degree in Education Policy from the University of Lakemont, where she was an Advanced Opportunity Fellow and a BA in education from Carrow College.</p>
  </section>

  <footer class="contact-bar">
    <svg viewBox="0 0 20 20" aria-hidden="true">
      <polygon points="3,15 13,5 16,8 6,18 2,19" fill="var(--paper)"/>
      <polygon points="14,4 16,2 19,5 17,7" fill="var(--paper)"/>
    </svg>
    If you have questions, please contact a member of our team at +27 79-000-4821 or by email at info@thabeniacademy
  </footer>

</body>
</html>
```